Infographic - Engagement Survey

Infographic required to be used in our marketing collateral and our website

Target Market(s)

B2B - commercial, non for profit, private, government and council

Industry/Entity Type

Marketing

Font styles to use
Sans Serif

Colors
0455a3
3276b5
85abd2
cedeed
e34197

Requirements
Must have
• Please refer to document for branding colours, fonts used are arial, calibri and century gothic

```html
<!DOCTYPE html>
<html lang="en">
<head>
<meta charset="utf-8">
<title>Job, Team, Leader, and Organisation Factors Predicting Engagement</title>
<link href="https://fonts.googleapis.com/css2?family=Lato:wght@400;700;900&display=swap" rel="stylesheet">
<style>
  :root {
    --navy: #353f6c;
    --pink: #cc3494;
    --blue: #5b9bd3;
    --gold: #e5a526;
    --light: #eff1f8;
    --white: #ffffff;
    --ink: #222222;
  }
  * { margin: 0; padding: 0; box-sizing: border-box; }
  html, body { width: 957px; height: 1200px; overflow: hidden; }
  body { font-family: 'Lato', Arial, sans-serif; color: var(--ink); background: var(--white); position: relative; }
  .masthead { position: absolute; left: 0; top: 0; width: 957px; height: 160px; background: var(--navy); }
  .masthead-title { position: absolute; left: 37px; top: 22px; color: var(--white); font-weight: 900; font-size: 35px; line-height: 40px; }
  .brand-name { position: absolute; right: 26px; top: 38px; color: var(--white); font-weight: 900; font-size: 38px; line-height: 42px; text-align: right; }
  .stripe { position: absolute; left: 0; width: 957px; }
  .stripe-pink-top { top: 160px; height: 8px; background: var(--pink); }
  .stripe-blue-top { top: 168px; height: 11px; background: var(--blue); }
  .band-measure { position: absolute; left: 0; top: 179px; width: 957px; height: 249px; background: var(--light); }
  .band-factors { position: absolute; left: 0; top: 428px; width: 957px; height: 360px; background: var(--white); }
  .band-predictors { position: absolute; left: 0; top: 788px; width: 957px; height: 282px; background: var(--light); }
  .band-summary { position: absolute; left: 0; top: 1070px; width: 957px; height: 112px; background: var(--white); }
  .measure-heading { position: absolute; left: 34px; top: 289px; font-size: 29px; font-weight: 900; color: var(--ink); }
  .graphic { position: absolute; left: 0; top: 0; width: 957px; height: 1200px; }
  .predictors-heading { position: absolute; right: 369px; top: 876px; text-align: right; font-size: 28px; line-height: 35px; font-weight: 900; color: var(--ink); }
  .beta-table { position: absolute; left: 604px; top: 826px; width: 318px; }
  .beta-head { display: flex; justify-content: space-between; padding: 0 6px 0 5px; font-size: 17px; font-weight: 700; height: 24px; }
  .beta-row { display: flex; justify-content: space-between; height: 21px; margin-bottom: 2.2px; padding: 0 6px 0 5px; color: var(--white); font-size: 13.5px; line-height: 21px; }
  .beta-row.job { background: var(--pink); }
  .beta-row.leader { background: var(--gold); }
  .beta-row.team { background: var(--navy); }
  .summary-heading { position: absolute; left: 19px; top: 1092px; font-size: 29px; line-height: 34px; font-weight: 900; color: var(--ink); }
  .summary-col { position: absolute; width: 140px; margin-left: -70px; text-align: center; font-size: 15px; line-height: 16px; }
  .summary-head { top: 1098px; }
  .summary-value { top: 1144px; }
  .summary-rule { position: absolute; left: 430px; top: 1133px; width: 511px; height: 3px; background: var(--navy); }
  .stripe-blue-bottom { top: 1182px; height: 6px; background: var(--blue); }
  .stripe-pink-bottom { top: 1188px; height: 6px; background: var(--pink); }
  .stripe-navy-bottom { top: 1194px; height: 6px; background: var(--navy); }
  .list-text { font-family: 'Lato', Arial, sans-serif; font-size: 12px; fill: var(--ink); }
  .segment-label { font-family: 'Lato', Arial, sans-serif; font-weight: 900; fill: var(--white); text-anchor: middle; }
  .pie-label { font-family: 'Lato', Arial, sans-serif; font-weight: 900; fill: var(--white); font-size: 27px; text-anchor: middle; }
  .pie-name { font-family: 'Lato', Arial, sans-serif; font-weight: 700; fill: var(--ink); font-size: 19px; text-anchor: middle; }
  .chevron-label { font-family: 'Lato', Arial, sans-serif; font-weight: 900; fill: var(--white); text-anchor: middle; }
</style>
</head>
<body>
  <header class="masthead">
    <h1 class="masthead-title">Job, Team, Leader,<br>and Organisation Factors<br>Predicting Engagement</h1>
    <div class="brand-name">Kestrel<br>Consulting</div>
  </header>
  <div class="stripe stripe-pink-top"></div>
  <div class="stripe stripe-blue-top"></div>

  <section class="band-measure"></section>
  <section class="band-factors"></section>
  <section class="band-predictors"></section>
  <section class="band-summary"></section>

  <h2 class="measure-heading">How do we Measure Engagement?</h2>

  <svg class="graphic" viewBox="0 0 957 1200" xmlns="http://www.w3.org/2000/svg">
    <!-- engagement measures -->
    <g class="chevron energy">
      <path d="M542,276 L603,214 L664,276 L664,400 L603,344 L542,400 Z" fill="var(--pink)"/>
      <circle cx="603" cy="272" r="20" fill="var(--white)"/>
      <path d="M607,259 L595,275 L602,275 L598,286 L611,269 L604,269 Z" fill="var(--pink)"/>
      <text class="chevron-label" x="603" y="327" font-size="28">ENERGY</text>
    </g>
    <g class="chevron commitment">
      <path d="M669,276 L730,214 L791,276 L791,400 L730,344 L669,400 Z" fill="var(--blue)"/>
      <circle cx="730" cy="272" r="20" fill="var(--white)"/>
      <path d="M720,272 L727,280 L741,264" fill="none" stroke="var(--blue)" stroke-width="5" stroke-linecap="round" stroke-linejoin="round"/>
      <text class="chevron-label" x="730" y="323" font-size="17">COMMITMENT</text>
    </g>
    <g class="chevron flow">
      <path d="M795,276 L856,214 L917,276 L917,400 L856,344 L795,400 Z" fill="var(--gold)"/>
      <circle cx="856" cy="272" r="20" fill="var(--white)"/>
      <path d="M845,268 q5.5,-5 11,0 t11,0 M845,276 q5.5,-5 11,0 t11,0" fill="none" stroke="var(--gold)" stroke-width="3" stroke-linecap="round"/>
      <text class="chevron-label" x="856" y="327" font-size="29">FLOW</text>
    </g>

    <!-- factor segments -->
    <path d="M309.5,770.1 A216,216 0 0 1 309.5,573.9 L420,630.2 A92,92 0 0 0 420,713.8 Z" fill="var(--navy)"/>
    <path d="M320.8,554.3 A216,216 0 0 1 494.4,456.2 L498.8,580.1 A92,92 0 0 0 424.8,621.9 Z" fill="var(--gold)"/>
    <path d="M509.6,456.2 A216,216 0 0 1 683.2,554.3 L579.2,621.9 A92,92 0 0 0 505.2,580.1 Z" fill="var(--pink)"/>
    <path d="M694.5,573.9 A216,216 0 0 1 694.5,770.1 L584,713.8 A92,92 0 0 0 584,630.2 Z" fill="var(--blue)"/>
    <text x="502" y="668" text-anchor="middle" font-family="Lato, Arial, sans-serif" font-size="19" fill="var(--ink)">What Affects</text>
    <text x="502" y="693" text-anchor="middle" font-family="Lato, Arial, sans-serif" font-size="21" font-weight="900" fill="var(--ink)">ENGAGEMENT</text>

    <!-- segment icons -->
    <g fill="var(--white)">
      <circle cx="430" cy="509" r="9"/><path d="M416,548 q0,-26 14,-26 q14,0 14,26 Z"/>
      <circle cx="410" cy="515" r="6"/><path d="M399,545 q0,-20 11,-20 q6,0 8,4 q-4,6 -4,16 Z"/>
      <circle cx="450" cy="515" r="6"/><path d="M461,545 q0,-20 -11,-20 q-6,0 -8,4 q4,6 4,16 Z"/>
      <rect x="553" y="510" width="50" height="36" rx="4"/>
      <rect x="570" y="503" width="16" height="9" rx="2" fill="none" stroke="var(--white)" stroke-width="3"/>
      <rect x="576" y="524" width="6" height="6" fill="var(--pink)"/>
      <rect x="625" y="625" width="40" height="60" rx="1"/>
      <rect x="636" y="616" width="18" height="10"/>
      <circle cx="358" cy="636" r="8"/><circle cx="344" cy="642" r="6"/><circle cx="372" cy="642" r="6"/>
      <path d="M348,652 h20 v28 h-20 Z M334,652 h10 v20 h-10 Z M372,652 h10 v20 h-10 Z"/>
    </g>
    <g fill="var(--blue)">
      <rect x="632" y="636" width="26" height="4"/><rect x="632" y="646" width="26" height="4"/>
      <rect x="632" y="656" width="26" height="4"/><rect x="632" y="666" width="26" height="4"/>
    </g>
    <text class="segment-label" x="430" y="571" font-size="19">LEADER</text>
    <text class="segment-label" x="578" y="575" font-size="28">JOB</text>
    <text class="segment-label" x="358" y="702" font-size="19">TEAM</text>
    <text class="segment-label" x="646" y="705" font-size="16">ORGANISATION</text>

    <!-- leader list -->
    <line x1="278" y1="462" x2="278" y2="608" stroke="var(--gold)" stroke-width="2"/>
    <g fill="var(--gold)">
      <circle cx="278" cy="462" r="3"/><circle cx="278" cy="477.5" r="3"/><circle cx="278" cy="493" r="3"/>
      <circle cx="278" cy="508.5" r="3"/><circle cx="278" cy="524" r="3"/><circle cx="278" cy="539.5" r="3"/>
      <circle cx="278" cy="555" r="3"/><circle cx="278" cy="570.5" r="3"/><circle cx="278" cy="586" r="3"/>
      <circle cx="278" cy="601.5" r="3"/>
    </g>
    <g class="list-text" text-anchor="end">
      <text x="272" y="466">Creates a learning environment</text>
      <text x="272" y="481.5">Supportive Leadership</text>
      <text x="272" y="497">Fosters teamwork</text>
      <text x="272" y="512.5">Encourages autonomous decision making</text>
      <text x="272" y="528">Creates clarity about appropriate behaviours</text>
      <text x="272" y="543.5">Effective management of behaviours</text>
      <text x="272" y="559">Creates clarity about performance standards</text>
      <text x="272" y="574.5">Effective management of underperformance</text>
      <text x="272" y="590">Celebrate success</text>
      <text x="272" y="605.5">Optimism and positivity</text>
    </g>

    <!-- team list -->
    <line x1="277" y1="651" x2="277" y2="723" stroke="var(--navy)" stroke-width="2"/>
    <g fill="var(--navy)">
      <circle cx="277" cy="655" r="3"/><circle cx="277" cy="670.5" r="3"/><circle cx="277" cy="686" r="3"/>
      <circle cx="277" cy="701.5" r="3"/><circle cx="277" cy="717" r="3"/>
    </g>
    <g class="list-text" text-anchor="end">
      <text x="270" y="659">Freedom to make decisions</text>
      <text x="270" y="674.5">Optimism</text>
      <text x="270" y="690">Customer Commitment</text>
      <text x="270" y="705.5">Performance feedback</text>
      <text x="270" y="721">Clarity of goals</text>
    </g>

    <!-- job list -->
    <line x1="726" y1="462" x2="726" y2="533" stroke="var(--pink)" stroke-width="2"/>
    <g fill="var(--pink)">
      <circle cx="726" cy="466" r="3"/><circle cx="726" cy="481.5" r="3"/><circle cx="726" cy="497" r="3"/>
      <circle cx="726" cy="512.5" r="3"/><circle cx="726" cy="528" r="3"/>
    </g>
    <g class="list-text">
      <text x="733" y="470">Optimism</text>
      <text x="733" y="485.5">Variety of Work</text>
      <text x="733" y="501">Self confidence</text>
      <text x="733" y="516.5">Learning at work</text>
      <text x="733" y="532">Knowledge of processes and policies</text>
    </g>

    <!-- organisation list -->
    <line x1="727" y1="612" x2="727" y2="730" stroke="var(--blue)" stroke-width="2"/>
    <g fill="var(--blue)">
      <circle cx="727" cy="617" r="3"/><circle cx="727" cy="632.5" r="3"/><circle cx="727" cy="648" r="3"/>
      <circle cx="727" cy="663.5" r="3"/><circle cx="727" cy="679" r="3"/><circle cx="727" cy="694.5" r="3"/>
      <circle cx="727" cy="710" r="3"/><circle cx="727" cy="725.5" r="3"/>
    </g>
    <g class="list-text">
      <text x="734" y="621">Optimism</text>
      <text x="734" y="636.5">Willingness to change</text>
      <text x="734" y="652">Encouragesment and support</text>
      <text x="734" y="667.5">Freedom to make decisions</text>
      <text x="734" y="683">Recognition of performance</text>
      <text x="734" y="698.5">Clarity of goals</text>
      <text x="734" y="714">Customer commitment</text>
      <text x="734" y="729.5">Performance feedback</text>
    </g>

    <!-- predictor pie -->
    <path d="M185,930 L132.5,1012.7 A98,98 0 1 1 283,930 Z" fill="var(--pink)"/>
    <path d="M185,930 L267.7,982.5 A98,98 0 0 1 132.5,1012.7 Z" fill="var(--navy)"/>
    <path d="M185,930 L283,930 A98,98 0 0 1 267.7,982.5 Z" fill="var(--gold)"/>
    <text class="pie-label" x="167" y="912">66%</text>
    <text class="pie-label" x="195" y="999">25%</text>
    <text class="pie-label" x="256" y="961">9%</text>
    <text class="pie-name" transform="translate(98,872) rotate(-58)">JOB</text>
    <text class="pie-name" transform="translate(300,962) rotate(-80)">LEADER</text>
    <text class="pie-name" transform="translate(202,1044) rotate(-8)">TEAM</text>
  </svg>

  <h2 class="predictors-heading">What areThe Best<br>Predictors<br>of Engagement?</h2>

  <div class="beta-table">
    <div class="beta-head"><span>Factor</span><span>Beta Weights</span></div>
    <div class="beta-row job"><span>(CB) Learning at Work</span><span>.257</span></div>
    <div class="beta-row job"><span>(CB) Optimism - Job</span><span>.238</span></div>
    <div class="beta-row job"><span>(CB) Self Confidence</span><span>.207</span></div>
    <div class="beta-row job"><span>(CB) Variety of Work</span><span>.189</span></div>
    <div class="beta-row leader"><span>(LB) Creates a Learning Environment</span><span>-.131</span></div>
    <div class="beta-row team"><span>(CB) Optimism - Team</span><span>.123</span></div>
    <div class="beta-row team"><span>(CB) Clarity of Goals - Team</span><span>.112</span></div>
    <div class="beta-row team"><span>(CB) Recognition of Performance - Team</span><span>.103</span></div>
  </div>

  <h2 class="summary-heading">Model<br>Summary</h2>
  <div class="summary-col summary-head" style="left:454px">Model</div>
  <div class="summary-col summary-head" style="left:536px">R</div>
  <div class="summary-col summary-head" style="left:629px">R Square</div>
  <div class="summary-col summary-head" style="left:745px">Adjusted<br>R Square</div>
  <div class="summary-col summary-head" style="left:890px">STD Error of<br>the Estimate</div>
  <div class="summary-rule"></div>
  <div class="summary-col summary-value" style="left:453px">1</div>
  <div class="summary-col summary-value" style="left:537px">.806</div>
  <div class="summary-col summary-value" style="left:625px">.650</div>
  <div class="summary-col summary-value" style="left:742px">.641</div>
  <div class="summary-col summary-value" style="left:890px">.64165</div>

  <div class="stripe stripe-blue-bottom"></div>
  <div class="stripe stripe-pink-bottom"></div>
  <div class="stripe stripe-navy-bottom"></div>
</body>
</html>
```